creative high tech business card design project

I am looking for a two(2) sided business card design for our computer software training company.

Who We Are
Tovrel Computer Training offers hands-on/instructor-led computer software training. We offer courses ranging from “Beginning Computers” to “Certification Prep”

Our Target Market:
Our target market is a very broad spectrum since we offer such a variety of courses catered to all groups. Previous student clientele has included the following:
Age range: 16-75
Demographic: recent high school graduates, college students, young professionals, office professionals, creative professionals, un-employed, seniors

prefer double sided card to be printed on paper or translucent plastic.

see uploaded logo for color scheme

Industry/Entity Type

High School

Requirements
Must have
• Must be double sided and include the following six (6) pieces
- logo (see uploaded files)
- Full Name
- Name@TovreltTraining.example
- (555) 555 - 8607
- www.TovrelTraining.example
- QR Code (see uploaded files)
Nice to have
• we'd prefer a semi-translucent plastic business card for examples please refer to http://www.lunacardworks.example/

Should not have
• Please upload each double sided design as ONE(1) submission.

Any entries that contains only a single side design will be eliminated.

```html
<!DOCTYPE html>
<html lang="en">
<head>
<meta charset="utf-8">
<title>Tovrel Computer Training – Business Card</title>
<link rel="stylesheet" href="https://fonts.googleapis.com/css2?family=Arimo:wght@400;700&display=swap">
<style>
  :root {
    --page: #ffffff;
    --card-dark: #2e3a4b;
    --card-mid: #29496a;
    --card-light: #1f5f8e;
    --band: rgba(20, 28, 40, 0.55);
    --rule: rgba(15, 22, 32, 0.6);
    --rule-light: rgba(120, 160, 200, 0.25);
    --brand: #4d8ab3;
    --text-light: #f2f4f7;
    --text-muted: #a7b1bf;
  }
  * { margin: 0; padding: 0; box-sizing: border-box; }
  html, body {
    width: 1000px;
    height: 1200px;
    overflow: hidden;
    background: var(--page);
    font-family: "Arimo", Arial, sans-serif;
  }
  .canvas { position: relative; width: 1000px; height: 1200px; }

  .card {
    position: absolute;
    width: 700px;
    height: 400px;
    overflow: hidden;
    background:
      radial-gradient(ellipse at 85% 15%, var(--card-light) 0%, transparent 65%),
      linear-gradient(100deg, var(--card-dark) 0%, var(--card-mid) 60%, var(--card-light) 100%);
  }
  .card--front { left: 130px; top: 70px; }
  .card--back { left: 112px; top: 604px; }

  .card__band {
    position: absolute;
    top: 0;
    left: 160px;
    width: 24px;
    background: var(--band);
  }
  .card--front .card__band { height: 290px; }
  .card--back .card__band { height: 180px; }

  .card__rule {
    position: absolute;
    left: 0;
    right: 0;
    top: 290px;
    height: 3px;
    background: var(--rule);
    border-bottom: 1px solid var(--rule-light);
  }

  .brand {
    position: absolute;
    color: var(--brand);
    font-weight: 700;
    text-align: center;
    line-height: 1;
  }
  .brand__name { display: block; }
  .brand__tag { display: block; }

  .card--front .brand { left: 0; right: 0; top: 24px; }
  .card--front .brand__name { font-size: 150px; letter-spacing: 12px; }
  .card--front .brand__tag { font-size: 26px; letter-spacing: 7px; margin-top: 14px; }

  .card--back .brand { left: 340px; width: 350px; top: 300px; }
  .card--back .brand__name { font-size: 72px; letter-spacing: 7px; }
  .card--back .brand__tag { font-size: 13px; letter-spacing: 4px; margin-top: 6px; }

  .intro {
    position: absolute;
    left: 0;
    right: 0;
    top: 291px;
    color: var(--text-light);
    font-size: 21px;
    line-height: 26px;
    text-align: center;
  }

  .contact {
    position: absolute;
    left: 0;
    top: 168px;
    list-style: none;
    color: var(--text-muted);
    font-size: 31px;
    line-height: 38px;
  }
  .contact__item { white-space: nowrap; }
  .contact__item--phone { padding-left: 74px; }
  .contact__item--web { padding-left: 24px; }
</style>
</head>
<body>
<main class="canvas">
  <section class="card card--front" aria-label="Card front">
    <div class="card__band"></div>
    <div class="card__rule"></div>
    <div class="brand">
      <span class="brand__name">TOVREL</span>
      <span class="brand__tag">COMPUTER TRAINING</span>
    </div>
    <p class="intro">
      Tovrel Computer Training offers hands-on/instructor-led<br>
      computer software training.<br>
      We offer courses ranging from “Beginning Computers”<br>
      to “Certification Prep”
    </p>
  </section>

  <section class="card card--back" aria-label="Card back">
    <div class="card__band"></div>
    <div class="card__rule"></div>
    <ul class="contact">
      <li class="contact__item contact__item--email">- Name@TovreltTraining.example</li>
      <li class="contact__item contact__item--phone">- (555) 555 - 8607</li>
      <li class="contact__item contact__item--web">- www.TovrelTraining.example</li>
    </ul>
    <div class="brand">
      <span class="brand__name">TOVREL</span>
      <span class="brand__tag">COMPUTER TRAINING</span>
    </div>
  </section>
</main>
</body>
</html>
```